ROB HOSE SOLUTIONS

Wrap designed for truck using rob hose logo colours, have yellow, blue, green water drops and hydraulics hoses. More colour.

Requirements
Must have
• Wrap designed for truck using rob hose logo colours, have yellow, blue, green water drops and hydraulics hoses. More colour.
Nice to have

```html
<!DOCTYPE html>
<html lang="en">
<head>
<meta charset="utf-8">
<title>Rob Hose Solutions – Truck Wrap</title>
<link href="https://fonts.googleapis.com/css2?family=Exo+2:wght@700;800&family=Russo+One&display=swap" rel="stylesheet">
<style>
  :root{
    --navy:#28306f;
    --blue:#2b4fb3;
    --green:#3f9a43;
    --white:#ffffff;
    --paper:#eef1f4;
    --edge:#d3d8df;
  }
  html,body{margin:0;padding:0;width:1200px;height:1200px;overflow:hidden;background:var(--paper);}
  .canvas{width:1200px;height:1200px;display:flex;flex-direction:column;justify-content:space-around;}
  .truck-side{display:block;width:1200px;height:540px;}
  .brand-name{font-family:"Exo 2",sans-serif;font-weight:800;fill:var(--navy);}
  .tagline{font-family:"Exo 2",sans-serif;font-weight:700;fill:var(--navy);font-size:19px;letter-spacing:.5px;}
  .tagline-small{font-family:"Exo 2",sans-serif;font-weight:700;fill:var(--navy);font-size:7px;letter-spacing:.2px;}
  .phone{font-family:"Russo One",sans-serif;fill:var(--white);font-size:34px;letter-spacing:1px;}
  .web{font-family:"Russo One",sans-serif;fill:var(--white);font-size:20px;}
</style>
</head>
<body>
<main class="canvas">

  <!-- Driver side -->
  <svg class="truck-side" viewBox="0 0 1200 540" xmlns="http://www.w3.org/2000/svg">
    <defs>
      <linearGradient id="metal" x1="0" y1="0" x2="1" y2="1">
        <stop offset="0" stop-color="#f2f4f6"/>
        <stop offset=".5" stop-color="#b9bfc6"/>
        <stop offset="1" stop-color="#8d949c"/>
      </linearGradient>
      <g id="wrap-shapes">
        <!-- cab panel -->
        <path class="cab-panel" d="M20,140 Q30,60 120,50 L380,50 L380,470 L20,470 Z" fill="var(--white)" stroke="var(--edge)" stroke-width="2"/>
        <path class="cab-swoosh-blue" d="M380,50 L340,50 L320,200 Q310,250 250,254 L80,262 Q45,264 46,300 L60,460 L96,460 L84,320 Q83,298 110,297 L300,290 Q370,285 380,220 Z" fill="var(--blue)"/>
        <path class="cab-swoosh-green" d="M380,220 L380,250 Q370,305 300,312 L125,320 Q106,322 108,345 L118,460 L98,460 L88,330 Q87,300 115,298 L300,290 Q370,285 380,220 Z" fill="var(--green)"/>
        <rect class="cab-base-blue" x="120" y="430" width="260" height="18" fill="var(--blue)"/>
        <rect class="cab-base-green" x="120" y="448" width="260" height="22" fill="var(--green)"/>

        <!-- box panel -->
        <rect class="box-panel" x="430" y="40" width="740" height="400" fill="var(--white)" stroke="var(--edge)" stroke-width="2"/>
        <rect class="box-top-band" x="430" y="40" width="740" height="28" fill="var(--navy)"/>
        <path class="box-top-green" d="M430,110 L470,78 L1170,78 L1170,84 L474,84 L430,118 Z" fill="var(--green)"/>
        <path class="box-corner-navy" d="M430,40 L520,40 L430,100 Z" fill="var(--navy)"/>
        <!-- right diagonal stripes -->
        <path class="diag-green" d="M1000,100 L1030,100 L1170,300 L1170,340 Z" fill="var(--green)"/>
        <path class="diag-navy" d="M1050,100 L1130,100 L1170,160 L1170,420 Z" fill="var(--navy)"/>
        <path class="diag-green-low" d="M980,140 L1010,140 L1150,395 L1120,395 Z" fill="var(--green)"/>
        <path class="hose-fittings" role="img" aria-label="Photo of three chrome hydraulic hose elbow fittings" d="M1040,110 L1160,110 L1160,380 L1120,380 L1020,200 Z" fill="url(#metal)"/>
        <!-- contact band -->
        <path class="contact-band" d="M790,320 L1110,320 L1140,395 L830,395 Z" fill="var(--navy)"/>
        <rect class="box-bottom-band" x="430" y="395" width="740" height="15" fill="var(--navy)"/>
        <rect class="box-skirt" x="430" y="410" width="740" height="30" fill="var(--green)"/>
        <rect class="side-locker" x="470" y="445" width="240" height="75" fill="var(--green)" stroke="#2f7a33" stroke-width="2"/>
      </g>
    </defs>
    <use href="#wrap-shapes"/>

    <text class="brand-name" x="640" y="235" font-size="74" text-anchor="middle">ROB HOSE</text>
    <text class="brand-name" x="640" y="284" font-size="40" text-anchor="middle">SOLUTIONS</text>
    <text class="tagline" x="640" y="316" text-anchor="middle">FUEL - AIR - WATER - OIL - GREASE</text>
    <text class="phone" x="965" y="360" text-anchor="middle">555-014-2273</text>
    <text class="web" x="975" y="386" text-anchor="middle">ROBHOSEPRO.COM</text>

    <text class="brand-name" x="240" y="382" font-size="24" text-anchor="middle">ROB HOSE</text>
    <text class="brand-name" x="240" y="398" font-size="13" text-anchor="middle">SOLUTIONS</text>
    <text class="tagline-small" x="240" y="410" text-anchor="middle">FUEL - AIR - WATER - OIL - GREASE</text>
  </svg>

  <!-- Passenger side -->
  <svg class="truck-side" viewBox="0 0 1200 540" xmlns="http://www.w3.org/2000/svg">
    <use href="#wrap-shapes" transform="translate(1200,0) scale(-1,1)"/>

    <text class="brand-name" x="560" y="235" font-size="74" text-anchor="middle">ROB HOSE</text>
    <text class="brand-name" x="560" y="284" font-size="40" text-anchor="middle">SOLUTIONS</text>
    <text class="tagline" x="560" y="316" text-anchor="middle">FUEL - AIR - WATER - OIL - GREASE</text>
    <text class="phone" x="235" y="360" text-anchor="middle">555-014-2273</text>
    <text class="web" x="225" y="386" text-anchor="middle">ROBHOSEPRO.COM</text>

    <text class="brand-name" x="960" y="382" font-size="24" text-anchor="middle">ROB HOSE</text>
    <text class="brand-name" x="960" y="398" font-size="13" text-anchor="middle">SOLUTIONS</text>
    <text class="tagline-small" x="960" y="410" text-anchor="middle">FUEL - AIR - WATER - OIL - GREASE</text>
  </svg>

</main>
</body>
</html>
```